Progressive business consultancy seeking innovative and clever powerpoint design

Were looking for a PowerPoint design for our Melbourne based business consulting company, Vantora.

About Us:
Based in Melbourne, Australia, Vantora is a management consulting organisation that partners with their clients to lead the execution of strategic process and system improvement initiatives.

Vantora offers business advisory services in Project Management, Business Process Management, Change Management, Business Analysis and Business Intelligence. Vantora combines hands on delivery with coaching in best practice methodologies and approaches to build our clients capabilities ensuring their ongoing success in project implementations.

Vantora has extensive experience across a wide range of industries. We specialise in assisting organisations across the accounting, legal, financial services and health sectors.

Our core purpose is to help businesses in the middle market navigate transformational change through clear and focused execution and enablement.

www.vantora.com.au
@vantora_hq

What we're looking for:
A PowerPoint template consisting of:
- a front/cover page with hero image (attached)
- a contents page
- a divider page (for different segments of the slide deck)
- a standard PowerPoint content page
- a blank PowerPoint page. (still Vantora themed)

The Vantora colours are white and blue (RGB:0/86/162 and
CMYK 97/73/4/0)

All slides should have the Vantora logo (attached) and a professional, almost corporate, (but not boring) theme that is consistent across all slides. The design should reflect our focus on the "e" in vantora, which is what we're really about - "e"xecution and "e"nablement of change.

I've attached a PNG file of our word template which shows the focus on the "e" as a watermark on the document as well as the font files if required.

Let me know if you need any further information or design specifics.

Thanks,

Marjorie
(on behalf of Desmond)
Updates

Project Deadline Extended
Reason: Hi Designers, We have received some really great designs. Thanks for taking the time to make your submissions. We have decided to extend the deadline as we need some more time to review and consult other colleagues on the great submissions we have received. We are also hoping we might get some additional submissions over the weekend. We would also like enough time to provide feedback on all the submissions received. Thanks for helping us out with some really creative work. Desmond @vantora_hq

Project Deadline Extended
Reason: Hi designers, thanks for taking the time to submit your designs. We have some really great submissions. We are going to have to extend our deadline again as we just haven't had the chance to review and provide feedback on all the designs. We will be closing this project off on Tuesday March 17. Thanks Desmond @vantora_hq

Target Market(s)

C-Level executives (CEO,COO,CIO) at professional services firms (Accounting and Legal), not for profit organisations and financial services firms.

Industry/Entity Type

Management Consulting

Font styles to use
Serif
Other font styles liked:
• Calibri or attached fonts

Requirements
Must have
• A PowerPoint template consisting of:
• 1) a front/cover page with hero image (attached)
• 2) a contents page
• 3) a divider page (for different segments of the slide deck)
• 4) a standard PowerPoint content page
• 5) a blank PowerPoint page. (still Vantora themed)
• 6) Two content
• 7) Comparison
• 8) Table
• 9) Picture column
• 10) Chevron
• The Vantora colours are white and blue (RGB:0/86/162 and
• CMYK 97/73/4/0)

```html
<!DOCTYPE html>
<html lang="en">
<head>
<meta charset="utf-8">
<title>Vantora – Slide Templates</title>
<link rel="stylesheet" href="https://fonts.googleapis.com/css2?family=Oswald:wght@500;600;700&family=Abel&family=Open+Sans:wght@400;600&display=swap">
<style>
  :root {
    --brand-blue: #0056a2;
    --band-blue: #0b57a6;
    --fold-blue: #22426b;
    --heading-blue: #0d4f9c;
    --ring-blue: #0a4589;
    --ink: #333333;
    --page: #ffffff;
    --backdrop: #efefef;
    --map-grey: #eef0f3;
  }
  * { margin: 0; padding: 0; box-sizing: border-box; }
  html, body { width: 849px; height: 1200px; overflow: hidden; }
  body { background: var(--backdrop); position: relative; font-family: "Abel", sans-serif; }

  .slide { position: absolute; background: var(--page); overflow: hidden; }
  .slide--agenda { left: 79px; top: 66px; width: 699px; height: 524px; }
  .slide--sections { left: 66px; top: 619px; width: 709px; height: 531px; }

  .brand-name {
    position: absolute; font-family: "Abel", sans-serif; font-size: 34px;
    color: var(--brand-blue); line-height: 1; letter-spacing: 1px;
  }
  .slide--agenda .brand-name { left: 511px; top: 48px; }
  .slide--sections .brand-name { left: 518px; top: 50px; }

  .page-number { position: absolute; font-family: "Abel", sans-serif; font-size: 17px; color: #222; line-height: 1; }
  .slide--agenda .page-number { left: 659px; top: 490px; }
  .slide--sections .page-number { left: 668px; top: 498px; }

  .agenda-steps { position: absolute; left: 0; top: 0; }
  .step-number { font-family: "Oswald", sans-serif; font-weight: 700; font-size: 26px; fill: #fff; }
  .step-label { font-family: "Open Sans", sans-serif; font-weight: 400; font-size: 11.5px; fill: #fff; letter-spacing: 0.4px; }

  .description { position: absolute; left: 450px; top: 193px; width: 240px; }
  .description-title {
    font-family: "Oswald", sans-serif; font-weight: 700; font-size: 27px; line-height: 33px;
    color: var(--heading-blue); text-transform: uppercase; transform: scaleX(0.94); transform-origin: left;
  }
  .description-text { margin-top: 2px; font-size: 15px; line-height: 16.5px; color: var(--ink); text-transform: uppercase; white-space: nowrap; }

  .map-area {
    position: absolute; left: 275px; top: 111px; width: 380px; height: 348px;
    background: var(--map-grey); border-radius: 42% 38% 30% 45% / 40% 45% 42% 40%;
  }
  .section-bands { position: absolute; left: 0; top: 0; }
  .section-number { font-family: "Oswald", sans-serif; font-weight: 700; font-size: 27px; fill: #fff; }

  .section-title {
    position: absolute; font-family: "Oswald", sans-serif; font-weight: 600; font-size: 19px;
    line-height: 1; color: var(--heading-blue); white-space: nowrap;
  }
  .section-text { position: absolute; font-size: 14.2px; line-height: 1; color: var(--ink); white-space: nowrap; }
</style>
</head>
<body>

<section class="slide slide--agenda">
  <div class="brand-name">Vantora</div>

  <svg class="agenda-steps" width="430" height="524" viewBox="0 0 430 524">
    <defs>
      <g id="step">
        <rect x="0" y="0" width="79" height="57" fill="var(--band-blue)"/>
        <polygon points="79,0 126,19 126,76 79,57" fill="var(--fold-blue)"/>
        <polygon points="126,19 397,19 419,47.5 397,76 126,76" fill="var(--band-blue)"/>
      </g>
    </defs>
    <g transform="translate(0,94)"><use href="#step"/><text class="step-number" x="40" y="39" text-anchor="middle">01</text><text class="step-label" x="272" y="52" text-anchor="middle">INSERT YOUR TEXT HERE</text></g>
    <g transform="translate(0,164)"><use href="#step"/><text class="step-number" x="40" y="39" text-anchor="middle">02</text><text class="step-label" x="272" y="52" text-anchor="middle">INSERT YOUR TEXT HERE</text></g>
    <g transform="translate(0,231)"><use href="#step"/><text class="step-number" x="40" y="39" text-anchor="middle">03</text><text class="step-label" x="272" y="52" text-anchor="middle">INSERT YOUR TEXT HERE</text></g>
    <g transform="translate(0,301)"><use href="#step"/><text class="step-number" x="40" y="39" text-anchor="middle">04</text><text class="step-label" x="272" y="52" text-anchor="middle">INSERT YOUR TEXT HERE</text></g>
    <g transform="translate(0,373)"><use href="#step"/><text class="step-number" x="40" y="39" text-anchor="middle">05</text><text class="step-label" x="272" y="52" text-anchor="middle">INSERT YOUR TEXT HERE</text></g>
  </svg>

  <div class="description">
    <h2 class="description-title">Here come is<br>your description<br>of the content</h2>
    <p class="description-text">With some expalnation on the<br>points or could be some<br>slogan of the company</p>
  </div>

  <div class="page-number">01</div>
</section>

<section class="slide slide--sections">
  <div class="map-area" role="img" aria-label="Faint map of Australia"></div>
  <div class="brand-name">Vantora</div>

  <svg class="section-bands" width="709" height="531" viewBox="0 0 709 531">
    <defs>
      <radialGradient id="disc" cx="50%" cy="30%" r="70%">
        <stop offset="0" stop-color="#3a8ad8"/>
        <stop offset="1" stop-color="#0a4a93"/>
      </radialGradient>
      <filter id="soft" x="-30%" y="-30%" width="160%" height="170%">
        <feDropShadow dx="0" dy="4" stdDeviation="3" flood-color="#000" flood-opacity="0.4"/>
      </filter>
      <g id="badge">
        <circle r="41" fill="var(--ring-blue)" filter="url(#soft)"/>
        <circle r="35" fill="#e8eef6"/>
        <circle r="33" fill="url(#disc)"/>
      </g>
    </defs>

    <rect x="0" y="136" width="130" height="41" fill="var(--band-blue)"/>
    <path d="M40 178 Q90 181 118 185" stroke="#222" stroke-width="3" fill="none" opacity="0.55"/>
    <use href="#badge" x="130" y="153"/>
    <text class="section-number" x="130" y="163" text-anchor="middle">01</text>

    <rect x="0" y="224" width="208" height="41" fill="var(--band-blue)"/>
    <path d="M110 266 Q165 269 196 273" stroke="#222" stroke-width="3" fill="none" opacity="0.55"/>
    <use href="#badge" x="208" y="241"/>
    <text class="section-number" x="208" y="251" text-anchor="middle">02</text>

    <rect x="0" y="313" width="270" height="41" fill="var(--band-blue)"/>
    <path d="M170 355 Q225 358 258 362" stroke="#222" stroke-width="3" fill="none" opacity="0.55"/>
    <use href="#badge" x="270" y="329"/>
    <text class="section-number" x="270" y="339" text-anchor="middle">03</text>

    <rect x="0" y="402" width="339" height="41" fill="var(--band-blue)"/>
    <path d="M240 444 Q295 447 327 451" stroke="#222" stroke-width="3" fill="none" opacity="0.55"/>
    <use href="#badge" x="339" y="419"/>
    <text class="section-number" x="339" y="429" text-anchor="middle">04</text>
  </svg>

  <h3 class="section-title" style="left:190px; top:129px;">Section title goes here</h3>
  <p class="section-text" style="left:215px; top:156px;">Insert text here with some description here</p>

  <h3 class="section-title" style="left:261px; top:218px;">Section title goes here</h3>
  <p class="section-text" style="left:283px; top:243px;">Insert text here with some description here</p>

  <h3 class="section-title" style="left:320px; top:307px;">Section title goes here</h3>
  <p class="section-text" style="left:344px; top:334px;">Insert text here with some description here</p>

  <h3 class="section-title" style="left:391px; top:396px;">Section title goes here</h3>
  <p class="section-text" style="left:412px; top:421px;">Insert text here with some description here</p>

  <div class="page-number">01</div>
</section>

</body>
</html>
```